TIDAL BODY CARE PACKAGING RENDERINGS

Logo and Packaging renderings for 4 core line Body Skin Care products called Tidal Glow. We make unisex natural skin care for the body. We would like designs that are very colorful and eye catching to communicate the humorous personality of the brand but communicate the efficacy and power of our formulations!

Target Market(s)

UNISEX, AGE 18 - 45, DRY SKIN, BLACK PEOPLE, NATURAL, CONSCIOUS CONSUMER

Industry/Entity Type

Cosmetics

Logo Text

TIDAL GLOW

Colors

Designer to choose colors to be used in the design.

Requirements
Must have
• BOLD CLEAR GRAPHICS
• COLOR (DIFFERENT COLORS PER PRODUCT)
Nice to have
• BLACK AND / OR WHITE WITH POPS OF BOLD COLOR
• BOLD COLOR OVERALL
• TYPOGRAPHIC ART STYLE

```html
<!DOCTYPE html>
<html lang="en">
<head>
<meta charset="utf-8">
<title>Tidal Glow – Hand &amp; Body Lotion</title>
<link href="https://fonts.googleapis.com/css2?family=Anton&family=Bowlby+One&family=Special+Elite&family=Roboto+Slab:wght@700&display=swap" rel="stylesheet">
<style>
  :root {
    --backdrop: #eceef1;
    --label-yellow: #f7d80c;
    --cap-yellow: #ecd00a;
    --brand-purple: #4e3a8e;
    --ink: #1d1d1b;
    --white: #ffffff;
  }
  html, body {
    margin: 0;
    padding: 0;
    width: 1200px;
    height: 1200px;
    overflow: hidden;
    background: var(--backdrop);
  }
  .canvas {
    position: relative;
    width: 1200px;
    height: 1200px;
  }
  .brand-mark {
    position: absolute;
    left: 128px;
    top: 520px;
    width: 330px;
    font-family: "Anton", sans-serif;
    color: var(--brand-purple);
    font-size: 78px;
    line-height: 0.95;
    letter-spacing: 2px;
  }
  .tube-label {
    position: absolute;
    left: 532px;
    top: 78px;
    width: 370px;
    height: 832px;
    background: var(--label-yellow);
  }
  .tube-cap {
    position: absolute;
    left: 600px;
    top: 916px;
    width: 228px;
    height: 152px;
    background: var(--cap-yellow);
    border-radius: 0 0 6px 6px;
  }
  .brand-band {
    position: absolute;
    left: 0;
    top: 0;
    width: 132px;
    height: 282px;
    background: var(--brand-purple);
  }
  .band-name {
    position: absolute;
    left: 0;
    top: 188px;
    width: 132px;
    text-align: center;
    font-family: "Anton", sans-serif;
    color: var(--white);
    font-size: 28px;
    line-height: 1;
    letter-spacing: 1px;
  }
  .product-name {
    position: absolute;
    left: 148px;
    top: 120px;
    font-family: "Anton", sans-serif;
    color: var(--brand-purple);
    font-size: 56px;
    line-height: 1.02;
    margin: 0;
  }
  .product-type {
    position: absolute;
    left: 148px;
    top: 238px;
    font-family: "Special Elite", monospace;
    color: var(--ink);
    font-size: 20px;
    line-height: 1.3;
    margin: 0;
  }
  .figure-art {
    position: absolute;
    background: var(--brand-purple);
  }
  .figure-art.before {
    left: 36px;
    top: 318px;
    width: 104px;
    height: 224px;
    border-radius: 48% 52% 30% 60% / 30% 40% 40% 50%;
    opacity: 0.85;
  }
  .figure-art.after {
    left: 212px;
    top: 522px;
    width: 104px;
    height: 224px;
    border-radius: 50% 50% 60% 30% / 30% 40% 50% 40%;
  }
  .claim-from {
    position: absolute;
    left: 172px;
    top: 356px;
    font-family: "Anton", sans-serif;
    color: var(--brand-purple);
    line-height: 1;
  }
  .claim-from .small { display: block; font-size: 32px; margin-left: 14px; }
  .claim-from .big { display: block; font-size: 48px; margin-top: 2px; }
  .transition-arrow {
    position: absolute;
    left: 140px;
    top: 450px;
  }
  .claim-to {
    position: absolute;
    left: 176px;
    top: 536px;
    font-family: "Bowlby One", sans-serif;
    color: var(--ink);
    font-size: 18px;
    transform: rotate(90deg);
  }
  .claim-result {
    position: absolute;
    left: 72px;
    top: 648px;
    font-family: "Bowlby One", sans-serif;
    color: var(--brand-purple);
    font-size: 46px;
    line-height: 1.05;
  }
  .claim-result .line-two { display: block; margin-left: 36px; }
  .usage-note {
    position: absolute;
    left: 240px;
    top: 758px;
    font-family: "Special Elite", monospace;
    color: var(--ink);
    font-size: 16px;
    line-height: 1.3;
    margin: 0;
  }
  .volume {
    position: absolute;
    left: 94px;
    top: 796px;
    font-family: "Roboto Slab", serif;
    font-weight: 700;
    color: var(--ink);
    font-size: 13px;
  }
</style>
</head>
<body>
<main class="canvas">
  <div class="brand-mark">TIDAL<br>GLOW</div>

  <section class="tube-label">
    <div class="brand-band">
      <div class="band-name">TIDAL<br>GLOW</div>
    </div>

    <h1 class="product-name">SO<br>LUSH!</h1>
    <p class="product-type">HAND &amp;<br>BODY LOTION</p>

    <div class="figure-art before" role="img" aria-label="Textured purple illustrated head in profile, the dry 'before' figure"></div>

    <div class="claim-from"><span class="small">From</span><span class="big">Ashy</span></div>

    <svg class="transition-arrow" width="120" height="190" viewBox="0 0 120 190" aria-hidden="true">
      <path d="M88 8 V78 H34 V160" fill="none" stroke="var(--ink)" stroke-width="10" stroke-linejoin="miter"/>
      <path d="M16 156 H52 L34 182 Z" fill="var(--ink)"/>
    </svg>
    <div class="claim-to">to</div>

    <div class="figure-art after" role="img" aria-label="Smooth purple illustrated head in profile, the moisturised 'after' figure"></div>

    <div class="claim-result">CLA<span class="line-two">SSY</span></div>

    <p class="usage-note">PUT IT<br>ON ME!</p>
    <div class="volume">200ml / 8.4 fl oz</div>
  </section>

  <div class="tube-cap"></div>
</main>
</body>
</html>
```